Label for Whiskey and Rum Bottle

We are a distillery. Whiskey and Rum We like to have a new label for our bottles. The whiskey bottles are in a wooden case. http://www.kornfaesser.ch/store/product/talwinkel-obermatt-single-malt-whiskey-nr-6 The Rum Bottles have no package. The label is even more important. http://www.kornfaesser.ch/store/product/talwinkel-obermatter-rum You can see the form of the bottles here www.kornfaesser.ch/store Whiskey and rum bottles are for a liter (50 cl) The labels can be with a picture or without. We would like to have something completely new. Therefore we don`t like to make much prescriptions concerning the design. We don`t like to give too much information (text) on the label. Just the information required by law. Consumers should understand the labels without long-reading. (The label-text is below) The 2 labels (Whiskey and rum) should look similar. Probably they have a different color or a different picture or .... It should be clear that the 2 products are from the same distillery. We have the intention to change all our existing labels over time. This gives designers the chance for follow-up projects.

Target Market(s)

Adults, liquor lovers

Requirements
Must have
• Information on the label is in German. (See "") Whiskey: - the name of the whiskey is "Talwinkel Obermatt Single Malt Whiskey" - The Whiskey was matured 5 years in a sherry "5 years in the sherry barrel stored" - The Alcohol content is 40% volumes "40% Vol "- The bottle contents 50 cl" 5 dl "- The distillery is" Distillery Brunnacher, Tornwil, www.kornfaesser.ch "- The producer is" Kelvor GmbH "Rum: - The name is" Talwinkel Obermatter Rum "- The alcohol content is 37% Volumes "37% Vol" - The bottle contens 50 cl "5 dl" - The distillery is "Distillery Brunnacher, Tornwil, www.kornfaesser.ch" - The producer is "Kelvor GmbH"
Nice to have
• Premium looking label Only front label preferred Only necessary text on the label
Should not have
• No special print techniques necessary No special paper form

```html
<!DOCTYPE html>
<html lang="de">
<head>
<meta charset="utf-8">
<title>Talwinkel Obermatter – Whiskey &amp; Rum Etiketten</title>
<link rel="stylesheet" href="https://fonts.googleapis.com/css2?family=Cinzel:wght@700;900&family=Archivo+Black&family=Oswald:wght@700&family=EB+Garamond:ital,wght@0,500;1,400&family=Roboto+Condensed:wght@700&display=swap">
<style>
  :root {
    --page: #e9e7e3;
    --whiskey-ground: #231f20;
    --rum-ground: #022a52;
    --gold: #c9a45c;
    --gold-light: #f3dc9c;
    --gold-dark: #8a6424;
    --cream: #fff9ea;
    --seal-red: #b3202a;
    --seal-dark: #6e0d14;
    --barrel-wood: #9a6a4a;
    --barrel-light: #d9c6b0;
  }
  * { box-sizing: border-box; margin: 0; padding: 0; }
  html, body { width: 1200px; height: 1200px; overflow: hidden; }
  body {
    background: var(--page);
    position: relative;
  }
  .label {
    position: absolute;
    top: 243px;
    width: 480px;
    height: 628px;
  }
  .label--whiskey { left: 90px; --ground: var(--whiskey-ground); }
  .label--rum { left: 630px; --ground: var(--rum-ground); }

  .label__frame {
    position: absolute;
    left: 0; top: 0;
    width: 480px; height: 720px;
    overflow: visible;
  }
  .brand {
    position: absolute;
    left: 0; right: 0;
    top: 36px;
    text-align: center;
    font-family: "Cinzel", serif;
    font-weight: 900;
    color: var(--cream);
    line-height: 56px;
    letter-spacing: 1px;
    text-shadow:
      1px 0 0 var(--gold-dark), -1px 0 0 var(--gold-dark),
      0 1px 0 var(--gold-dark), 0 -1px 0 var(--gold-dark),
      0 2px 2px rgba(0,0,0,.5);
  }
  .brand__line { display: block; }
  .brand__line--first { font-size: 40px; }
  .brand__line--second { font-size: 40px; }

  .dots {
    position: absolute;
    left: 50%;
    transform: translateX(-50%);
    border-top: 4px dotted var(--gold);
  }
  .dots--short { top: 158px; width: 150px; }
  .dots--long { width: 350px; }
  .label--whiskey .dots--long { top: 340px; }
  .label--rum .dots--long { top: 358px; }

  .ribbon {
    position: absolute;
    left: 50%;
    top: 180px;
    transform: translateX(-50%);
    overflow: visible;
  }
  .ribbon text {
    font-family: "Cinzel", serif;
    font-weight: 700;
    font-size: 17px;
    letter-spacing: 1.5px;
    fill: var(--cream);
  }

  .product {
    position: absolute;
    left: 0; right: 0;
    text-align: center;
    color: var(--cream);
    text-shadow:
      2px 0 0 var(--gold), -2px 0 0 var(--gold),
      0 2px 0 var(--gold), 0 -2px 0 var(--gold),
      0 3px 3px rgba(0,0,0,.5);
  }
  .product--whiskey {
    top: 262px;
    font-family: "Archivo Black", sans-serif;
    font-size: 62px;
    line-height: 70px;
    letter-spacing: 1px;
  }
  .product--rum {
    top: 248px;
    font-family: "Oswald", sans-serif;
    font-weight: 700;
    font-size: 92px;
    line-height: 100px;
    letter-spacing: 2px;
  }

  .barrels {
    position: absolute;
    width: 180px;
    height: 162px;
    left: 150px;
    border-radius: 60px 60px 40px 40px;
    background: radial-gradient(ellipse at 55% 40%, var(--barrel-light) 0%, var(--barrel-wood) 70%, transparent 72%);
  }
  .label--whiskey .barrels { top: 358px; }
  .label--rum .barrels { top: 388px; }

  .maker {
    position: absolute;
    left: 30px;
    top: 551px;
    font-family: "EB Garamond", serif;
    font-style: italic;
    font-size: 11px;
    line-height: 14px;
    color: var(--cream);
  }
  .volume {
    position: absolute;
    right: 30px;
    top: 582px;
    font-family: "Roboto Condensed", sans-serif;
    font-weight: 700;
    font-size: 17px;
    color: var(--cream);
    letter-spacing: .3px;
  }

  .seal {
    position: absolute;
    left: 176px;
    top: 515px;
    width: 130px;
    height: 130px;
    border-radius: 50%;
    background: radial-gradient(circle at 45% 40%, #d8343c 0%, var(--seal-red) 45%, var(--seal-dark) 100%);
    box-shadow: 0 2px 4px rgba(0,0,0,.45);
  }
  .seal__text {
    position: absolute;
    left: 176px;
    top: 534px;
    width: 130px;
    text-align: center;
    font-family: "EB Garamond", serif;
    font-weight: 500;
    color: var(--cream);
  }
  .seal__years { display: block; font-size: 46px; line-height: 44px; }
  .seal__unit { display: block; font-size: 21px; line-height: 24px; letter-spacing: 1px; }

  .cask-note {
    position: absolute;
    left: 0; top: 0;
    overflow: visible;
  }
  .cask-note text {
    font-family: "EB Garamond", serif;
    font-style: italic;
    font-size: 14px;
    fill: var(--cream);
  }
</style>
</head>
<body>

<!-- WHISKEY -->
<section class="label label--whiskey">
  <svg class="label__frame" viewBox="0 0 480 720" aria-hidden="true">
    <defs>
      <linearGradient id="goldEdgeW" x1="0" y1="0" x2="1" y2="1">
        <stop offset="0" stop-color="#f3dc9c"/>
        <stop offset=".45" stop-color="#b88a3e"/>
        <stop offset=".7" stop-color="#f0d596"/>
        <stop offset="1" stop-color="#8a6424"/>
      </linearGradient>
    </defs>
    <path d="M14,2 H466 a12,12 0 0 1 12,12 V614 a12,12 0 0 1 -12,12 H346 C346,682 298,713 241,713 C184,713 136,682 136,626 H14 a12,12 0 0 1 -12,-12 V14 a12,12 0 0 1 12,-12 Z"
          fill="var(--whiskey-ground)" stroke="#ffffff" stroke-width="14"/>
    <path d="M14,2 H466 a12,12 0 0 1 12,12 V614 a12,12 0 0 1 -12,12 H346 C346,682 298,713 241,713 C184,713 136,682 136,626 H14 a12,12 0 0 1 -12,-12 V14 a12,12 0 0 1 12,-12 Z"
          fill="none" stroke="url(#goldEdgeW)" stroke-width="7"/>
  </svg>

  <h1 class="brand">
    <span class="brand__line brand__line--first">TALWINKEL</span>
    <span class="brand__line brand__line--second">OBERMATTER</span>
  </h1>
  <div class="dots dots--short"></div>

  <svg class="ribbon" width="212" height="78" viewBox="0 0 212 78" aria-hidden="false">
    <path d="M0,22 Q106,-4 212,22 L212,74 Q106,48 0,74 Z" fill="var(--gold)"/>
    <path d="M7,27 Q106,4 205,27 L205,67 Q106,44 7,67 Z" fill="var(--whiskey-ground)" stroke="var(--gold-light)" stroke-width="1.5"/>
    <path id="ribbonArcW" d="M20,54 Q106,30 192,54" fill="none"/>
    <text text-anchor="middle"><textPath href="#ribbonArcW" startOffset="50%">SINGLE MALT</textPath></text>
  </svg>

  <h2 class="product product--whiskey">WHISKEY</h2>
  <div class="dots dots--long"></div>

  <div class="barrels" role="img" aria-label="Gestochene Illustration von drei gestapelten Holzfässern"></div>

  <p class="maker">Brennerei Brunnacher,<br>Tornwil Distilleries<br>www.kornfaesser.ch<br>Produced by Kelvor GmbH</p>
  <p class="volume">50cl &nbsp;/ 40%</p>

  <div class="seal" role="img" aria-label="Rotes Wachssiegel"></div>
  <p class="seal__text"><span class="seal__years">5</span><span class="seal__unit">JAHRE</span></p>

  <svg class="cask-note" width="480" height="720" viewBox="0 0 480 720" aria-hidden="false">
    <path id="caskArc" d="M160,640 Q241,735 322,640" fill="none"/>
    <text text-anchor="middle"><textPath href="#caskArc" startOffset="50%">im Sherry Fass gelagert</textPath></text>
  </svg>
</section>

<!-- RUM -->
<section class="label label--rum">
  <svg class="label__frame" viewBox="0 0 480 720" aria-hidden="true">
    <defs>
      <linearGradient id="goldEdgeR" x1="0" y1="0" x2="1" y2="1">
        <stop offset="0" stop-color="#f3dc9c"/>
        <stop offset=".45" stop-color="#b88a3e"/>
        <stop offset=".7" stop-color="#f0d596"/>
        <stop offset="1" stop-color="#8a6424"/>
      </linearGradient>
    </defs>
    <rect x="2" y="2" width="476" height="624" rx="12" fill="var(--rum-ground)" stroke="#ffffff" stroke-width="14"/>
    <rect x="2" y="2" width="476" height="624" rx="12" fill="none" stroke="url(#goldEdgeR)" stroke-width="7"/>
  </svg>

  <h1 class="brand">
    <span class="brand__line brand__line--first">TALWINKEL</span>
    <span class="brand__line brand__line--second">OBERMATTER</span>
  </h1>
  <div class="dots dots--short"></div>

  <svg class="ribbon" width="258" height="86" viewBox="0 0 258 86" aria-hidden="false">
    <path d="M0,26 Q129,-4 258,26 L258,82 Q129,52 0,82 Z" fill="var(--gold)"/>
    <path d="M7,31 Q129,4 251,31 L251,74 Q129,47 7,74 Z" fill="var(--rum-ground)" stroke="var(--gold-light)" stroke-width="1.5"/>
    <path id="ribbonArcR" d="M20,60 Q129,32 238,60" fill="none"/>
    <text text-anchor="middle"><textPath href="#ribbonArcR" startOffset="50%">SUPERIOR QUALITY</textPath></text>
  </svg>

  <h2 class="product product--rum">RUM</h2>
  <div class="dots dots--long"></div>

  <div class="barrels" role="img" aria-label="Gestochene Illustration von drei gestapelten Holzfässern"></div>

  <p class="maker">Brennerei Brunnacher,<br>Tornwil Distilleries<br>www.kornfaesser.ch<br>Produced by Kelvor GmbH</p>
  <p class="volume">50cl &nbsp;/ 40%</p>
</section>

</body>
</html>
```